Business Cards for a law firm

Business cards for our law firm. Use our silhoette logo and OAK HARBOR - check our website (www.oakharbor-legal.com)

Contact Information for Business Card

our silhouette logo, OAK HARBOR, 800-555-0147, Dorian Kestrup, dorian@oakharbor-legal.com

Requirements
Must have
• our silhouette logo, OAK HARBOR, 800-555-0147, Dorian Kestrup, dorian@oakharbor-legal.com

```html
<!DOCTYPE html>
<html lang="en">
<head>
<meta charset="UTF-8">
<title>Oak Harbor — Business Cards</title>
<link rel="stylesheet" href="https://fonts.googleapis.com/css2?family=Krona+One&family=Roboto:wght@400&display=swap">
<style>
  :root {
    --navy: #132a63;
    --navy-deep: #0f2050;
    --navy-light: #3a5db0;
    --paper: #f7f7f5;
    --ink-grey: #4a4a4a;
    --backdrop: #1b1b1d;
    --white: #ffffff;
  }
  * { margin: 0; padding: 0; box-sizing: border-box; }
  html, body {
    width: 1200px;
    height: 963px;
    overflow: hidden;
    background: var(--backdrop);
  }
  .sheet {
    position: relative;
    width: 1200px;
    height: 963px;
  }
  .card {
    position: absolute;
    left: 250px;
    width: 700px;
    height: 400px;
    overflow: hidden;
    box-shadow: 0 14px 30px rgba(0,0,0,0.5);
  }
  .card--front { top: 61px; background: var(--paper); }
  .card--back { top: 502px; background: var(--navy); }

  /* Front */
  .firm-title {
    position: absolute;
    left: 230px;
    top: 58px;
    font-family: "Krona One", sans-serif;
    font-size: 34px;
    letter-spacing: 1px;
    color: var(--navy);
  }
  .person-name {
    position: absolute;
    left: 124px;
    top: 196px;
    font-family: "Krona One", sans-serif;
    font-size: 20px;
    color: var(--navy);
  }
  .contact-list {
    position: absolute;
    left: 96px;
    top: 236px;
    list-style: none;
  }
  .contact-list li {
    display: flex;
    align-items: center;
    gap: 10px;
    height: 30px;
    font-family: "Roboto", sans-serif;
    font-size: 19px;
    color: var(--ink-grey);
  }
  .contact-list svg { width: 18px; height: 18px; flex: none; }
  .figure-front {
    position: absolute;
    left: 450px;
    top: 120px;
    width: 210px;
    height: 280px;
    border-radius: 90px 90px 0 0;
    background: linear-gradient(180deg, var(--navy) 0%, #1b3479 100%);
  }

  /* Back */
  .figure-back {
    position: absolute;
    left: 30px;
    top: 0;
    width: 200px;
    height: 400px;
    border-radius: 0 0 40px 40px;
    background: linear-gradient(180deg, var(--navy-deep) 0%, #1a2f6e 55%, var(--navy-light) 100%);
  }
  .brand-mark {
    position: absolute;
    left: 290px;
    top: 182px;
    display: flex;
    align-items: center;
    gap: 16px;
  }
  .brand-mark .dot {
    width: 34px;
    height: 34px;
    border-radius: 50%;
    background: var(--white);
  }
  .brand-mark .brand-name {
    font-family: "Krona One", sans-serif;
    font-size: 30px;
    letter-spacing: 1px;
    color: var(--white);
  }
</style>
</head>
<body>
<main class="sheet">
  <section class="card card--front" aria-label="Business card front">
    <h1 class="firm-title">OAK HARBOR</h1>
    <h2 class="person-name">DORIAN KESTRUP</h2>
    <ul class="contact-list">
      <li>
        <svg viewBox="0 0 24 24" aria-hidden="true"><path fill="#132a63" d="M6.6 10.8a15.1 15.1 0 0 0 6.6 6.6l2.2-2.2c.3-.3.7-.4 1-.2 1.1.4 2.3.6 3.6.6.6 0 1 .4 1 1V20c0 .6-.4 1-1 1C10.6 21 3 13.4 3 4c0-.6.4-1 1-1h3.5c.6 0 1 .4 1 1 0 1.3.2 2.5.6 3.6.1.3 0 .7-.2 1z"/></svg>
        800-555-0147
      </li>
      <li>
        <svg viewBox="0 0 24 24" aria-hidden="true"><rect x="2" y="5" width="20" height="14" rx="2" fill="#132a63"/><path d="M3 6l9 7 9-7" fill="none" stroke="#f7f7f5" stroke-width="1.8"/></svg>
        dorian@oakharbor-legal.com
      </li>
      <li>
        <svg viewBox="0 0 24 24" aria-hidden="true"><circle cx="12" cy="12" r="10" fill="#132a63"/><path d="M2 12h20M12 2c3 3 3 17 0 20M12 2c-3 3-3 17 0 20" fill="none" stroke="#f7f7f5" stroke-width="1.4"/></svg>
        www.oakharbor-legal.com
      </li>
    </ul>
    <div class="figure-front" role="img" aria-label="Navy silhouette of a standing man with hands in pockets"></div>
  </section>

  <section class="card card--back" aria-label="Business card back">
    <div class="figure-back" role="img" aria-label="Faint navy silhouette of a standing man fading to lighter blue"></div>
    <div class="brand-mark">
      <span class="dot" aria-hidden="true"></span>
      <span class="brand-name">OAK HARBOR</span>
    </div>
  </section>
</main>
</body>
</html>
```